Northfield Energy Product Distribution Brochure

We are looking to have our current brochure for our customers completely redesigned...the idea is to present the relevant information in an attractive way . Our website is northfieldenergy-example.com where you can find more information about us. We have included a file with a rough idea of the page order and what each should include but feel free to adapt based on design. The example provided is only for context and doesnt have to be maintained. We will be using the brochure both digitally and in print form. As long as it reads easily and is eye catching, the design can be horizontal or vertical.Final deliverable should be indesign file.

"Our Brands" page: should be limited to one page (space being enough) where it has the header for each one (for example diesel generators) space for one or two lines of text and then the corresponding logos for each of the five categories
Updates

For those asking: the "our brands" page should be a single page layout where there is a header with the corresponding section and space for maybe one line of text followed by the two logos for that category. Each of the product pages should be similar in fashion to the one in the document attached: a photo of the product with some white space and space for the text to be included. We will be posting additional examples today

Target Market(s)

We want to present it to customers both digitally and in print so they can see our products

Industry/Entity Type

Power Generation

Font styles to use
Serif

Requirements
Must have
• Eye catching and able to present the information in a presentable fashion. Rest is up to you.
Nice to have
• Should incorporate the colors of our logo but can also add other depending on design

```html
<!DOCTYPE html>
<html lang="en">
<head>
<meta charset="utf-8">
<title>Northfield Energy – Distributor Program Guide</title>
<link rel="stylesheet" href="https://fonts.googleapis.com/css2?family=Montserrat:wght@300;400;500;600;700;800&display=swap">
<style>
  :root{
    --gold:#f2b52a;
    --charcoal:#232323;
    --ink:#3e3e3e;
    --grey-page:#e9e9e9;
    --canvas:#dcdcdc;
    --partner-ink:#3a3a3a;
  }
  *{box-sizing:border-box;margin:0;padding:0}
  html,body{width:1200px;height:900px;overflow:hidden;background:var(--canvas);font-family:"Montserrat",sans-serif;color:var(--ink)}
  .spread{position:absolute;display:flex;box-shadow:0 6px 18px rgba(0,0,0,.12)}
  .page{position:relative;overflow:hidden}

  /* cover spread */
  .cover-spread{left:200px;top:40px;width:800px;height:300px}
  .cover-spread .page{width:400px;height:300px}
  .back-cover{background:var(--grey-page)}
  .back-cover .dark-band{position:absolute;left:0;right:0;top:190px;bottom:0;background:var(--charcoal)}
  .back-cover .gold-frame{position:absolute;left:40px;top:50px;width:320px;height:230px;border:2px solid var(--gold)}
  .brand-lockup{position:absolute;display:flex;align-items:center;gap:8px}
  .brand-mark{width:22px;height:22px;background:var(--gold)}
  .brand-name{font-weight:600;letter-spacing:.04em;color:#6a6a6a;font-size:15px;white-space:nowrap}
  .back-cover .brand-lockup{left:0;right:0;top:120px;justify-content:center}
  .contact{position:absolute;left:0;right:0;top:208px;text-align:center;color:var(--gold)}
  .contact h3{font-size:13px;font-weight:600;margin-bottom:12px}
  .contact p{font-size:10px;line-height:1.8}

  .front-cover{background:#efefef}
  .front-cover svg{position:absolute;inset:0}
  .cover-photo{position:absolute;left:175px;top:0;width:225px;height:165px;background:linear-gradient(135deg,#f4f4f4 0%,#cfcfcf 55%,#5a5a5a 100%)}
  .cover-title{position:absolute;left:205px;top:150px;color:var(--gold);font-weight:700;font-size:21px;line-height:1.05;letter-spacing:.02em}
  .cover-sub{position:absolute;left:205px;top:222px;color:#cfcfcf;font-size:7.5px;white-space:nowrap}
  .front-cover .brand-lockup{left:42px;top:200px;gap:6px}
  .front-cover .brand-mark{width:14px;height:14px}
  .front-cover .brand-name{font-size:10px;color:#9a9a9a}
  .perks{position:absolute;left:105px;top:256px;display:flex;gap:26px}
  .perk{display:flex;flex-direction:column;align-items:center;gap:3px;font-size:6px;color:#555;text-align:center;width:40px}
  .perk svg{position:static;width:18px;height:18px}

  /* inner spread */
  .inner-spread{left:110px;top:385px;width:980px;height:400px}
  .inner-spread .page{width:490px;height:400px}
  .product-page{background:linear-gradient(90deg,#f7f7f7 0%,#e6e6e6 70%,#d9d9d9 100%)}
  .product-photo{position:absolute;left:32px;top:18px;width:158px;height:320px;background:linear-gradient(90deg,#d8d4cf,#c4bfba)}
  .product-title{position:absolute;left:228px;top:58px;font-size:27px;line-height:1.25;color:#444}
  .product-title .light{font-weight:300;display:block}
  .product-title .bold{font-weight:700;display:block}
  .features-head{position:absolute;left:226px;top:160px;font-size:15px;font-weight:500;color:#444}
  .features{position:absolute;left:228px;top:195px;list-style:none;width:210px}
  .features li{position:relative;padding-left:9px;font-size:6.5px;line-height:1.55;color:#333;margin-bottom:12px}
  .features li::before{content:"✔";position:absolute;left:0;top:0;font-size:7px}
  .page-num{position:absolute;bottom:12px;font-size:13px;color:#333}
  .product-page .page-num{left:12px}
  .dark-bar{position:absolute;left:202px;bottom:10px;width:288px;height:20px;background:#4b4547}

  .distributor-page{background:linear-gradient(90deg,#e2e2e2 0%,#f3f3f3 25%,#f7f7f7 100%)}
  .section-tag{position:absolute;left:115px;top:0;width:372px;height:40px;background:var(--gold);color:#fff;font-size:22px;font-weight:600;padding:10px 0 0 12px;letter-spacing:.01em}
  .section-title{position:absolute;left:128px;top:40px;font-size:22px;font-weight:700;color:#4a4a4a}
  .benefits{position:absolute;left:26px;top:72px;width:444px;display:grid;grid-template-columns:1fr 1fr;gap:4px}
  .benefits div{height:34px;padding:5px 10px;font-size:6.3px;line-height:1.3;color:#3a3a3a;display:flex;flex-direction:column;justify-content:center}
  .row1{background:#e1e1e1}.row2{background:#d3d3d3}.row3{background:#c4c4c4}
  .row4{background:#b3b3b3}.row5{background:#a2a2a2}.row6{background:#929292}
  .partners{position:absolute;left:60px;top:306px;width:400px;display:flex;align-items:center;justify-content:space-around}
  .partner{font-weight:700;font-size:14px;letter-spacing:.04em;color:var(--partner-ink)}
  .gold-bar{position:absolute;left:0;bottom:10px;width:300px;height:20px;background:var(--gold)}
  .distributor-page .page-num{right:12px}
</style>
</head>
<body>

<section class="spread cover-spread">
  <article class="page back-cover">
    <div class="dark-band"></div>
    <div class="gold-frame"></div>
    <div class="brand-lockup"><span class="brand-mark"></span><span class="brand-name">NORTHFIELD ENERGY</span></div>
    <div class="contact">
      <h3>Contact Us</h3>
      <p>4418 Harbor Line Rd, Eastport, FL 33010</p>
      <p>(555) 010-0199</p>
    </div>
  </article>

  <article class="page front-cover">
    <div class="cover-photo" role="img" aria-label="Photo of a white trailer-mounted diesel generator"></div>
    <svg viewBox="0 0 400 300" width="400" height="300" aria-hidden="true">
      <path d="M0 20 Q60 0 120 10 Q70 40 40 120 L0 150 Z" fill="#f2b52a"/>
      <path d="M0 40 Q60 25 110 18 Q60 60 30 130 L0 150 Z" fill="#d9d9d9"/>
      <path d="M30 170 L400 120 L400 200 L330 240 L30 250 Z" fill="#2e2e2e"/>
      <path d="M290 300 L400 300 L400 185 Z" fill="#f2b52a"/>
      <rect x="95" y="250" width="200" height="50" fill="#ffffff"/>
    </svg>
    <div class="cover-title">DISTRIBUTOR<br>PROGRAM<br>GUIDE</div>
    <div class="cover-sub">Diesel Generators | Alternators | Parts</div>
    <div class="brand-lockup"><span class="brand-mark"></span><span class="brand-name">NORTHFIELD ENERGY</span></div>
    <div class="perks">
      <div class="perk">
        <svg viewBox="0 0 20 20"><circle cx="10" cy="6" r="3.5" fill="none" stroke="#777"/><path d="M3 18 Q10 9 17 18" fill="none" stroke="#777"/></svg>
        TEAM OF EXPERTS
      </div>
      <div class="perk">
        <svg viewBox="0 0 20 20"><circle cx="10" cy="10" r="7.5" fill="none" stroke="#777"/><path d="M10 5 V10 L13 12" fill="none" stroke="#777"/></svg>
        SAME DAY URGENCY
      </div>
      <div class="perk">
        <svg viewBox="0 0 20 20"><circle cx="10" cy="10" r="4" fill="none" stroke="#777"/><circle cx="10" cy="10" r="8" fill="none" stroke="#777" stroke-dasharray="3 2"/></svg>
        100% ORIGINAL
      </div>
    </div>
  </article>
</section>

<section class="spread inner-spread">
  <article class="page product-page">
    <div class="product-photo" role="img" aria-label="Photo of a grey wall-mounted transfer switch cabinet"></div>
    <h2 class="product-title"><span class="light">Transfer</span><span class="bold">Switches</span></h2>
    <h3 class="features-head">FEATURES</h3>
    <ul class="features">
      <li>Lorem ipsum dolor sit amet, consectetur adipiscing elit, sed do eiusmod tempor incididunt</li>
      <li>Lorem ipsum dolor sit amet, consectetur adipiscing elit, sed do eiusmod tempor incididunt</li>
      <li>Lorem ipsum dolor sit amet, consectetur adipiscing elit, sed do eiusmod tempor incididunt</li>
      <li>Lorem ipsum dolor sit amet, consectetur adipiscing elit, sed do eiusmod tempor incididunt</li>
    </ul>
    <div class="dark-bar"></div>
    <span class="page-num">12</span>
  </article>

  <article class="page distributor-page">
    <div class="section-tag">ALTERNATOR AND PARTS</div>
    <h2 class="section-title">DISTRIBUTOR</h2>
    <div class="benefits">
      <div class="row1">Buy direct from Corvane's Official Master distributor for The Americas</div>
      <div class="row1">30-minute-or-less™ response time for all pricing and availability requests (Monday thru Saturday)</div>
      <div class="row2">Buy direct from Halbrook's Official Parts Distributor for The Americas</div>
      <div class="row2">Halbrook same-day shipping on all stock orders (cutoff time 4:00PM EST)</div>
      <div class="row3">Direct access to the largest stock of Halbrook and Corvane Alternators &amp; Parts in The Americas</div>
      <div class="row3">Extended same-day shipping service available on all stock orders (cutoff time 6:00PM EST)</div>
      <div class="row4">1 Hour response time for other quotes (during business hours 8:30 am to 5:30 pm EST)</div>
      <div class="row4">Extended same-day shipping service available on all stock orders (cutoff time 6:00PM EST)</div>
      <div class="row5">Comprehensive online information library including datasheets, manuals, diagrams, high resolution photos, video tutorials, and more</div>
      <div class="row5"><span>Worldwide drop-shipping and blind-shipping available</span><span>Lead/Customer referral program (for selected and qualified accounts)</span></div>
      <div class="row6">Comprehensive online account access including: retail pricing, distributor discounts, bulk discounts, account management, order status, order history, and more</div>
      <div class="row6">Comprehensive online training and certification program</div>
    </div>
    <div class="partners">
      <span class="partner">DELMAR</span>
      <span class="partner">HALBROOK</span>
      <span class="partner">VEKTRA</span>
      <span class="partner">CORVANE</span>
    </div>
    <div class="gold-bar"></div>
    <span class="page-num">13</span>
  </article>
</section>

</body>
</html>
```